Mabel's Fitness Business Cards

I would like my business cards to look expensive and sophisticated using my logo and the information below.

FRONT
Mabel’s Fitness logo

Tag line Become your happiest, healthiest and strongest self

Mabel Quint Harlow
Personal Trainer

e. mabel@mabelsfitstudio.example

t. 0781530462

w. www.mabelsfitstudio.example

```html
<!DOCTYPE html>
<html lang="en">
<head>
<meta charset="utf-8">
<title>Mabel’s Fitness Business Cards</title>
<link href="https://fonts.googleapis.com/css2?family=Roboto:ital,wght@0,300;0,400;0,500;1,700&display=swap" rel="stylesheet">
<style>
  :root {
    --backdrop: #3a3a3a;
    --card: #1b1c1e;
    --silver: #b9b9bb;
    --teal: #6cc3cf;
    --stone: #b3aca8;
    --muted: #9a9a9c;
    --rule: #5aa9b5;
  }
  * { box-sizing: border-box; margin: 0; padding: 0; }
  html, body { width: 799px; height: 1200px; overflow: hidden; }
  body {
    background: var(--backdrop);
    font-family: "Roboto", Arial, sans-serif;
    position: relative;
  }
  .card {
    position: absolute;
    left: 90px;
    width: 620px;
    height: 354px;
    background: var(--card);
    border-radius: 4px;
    box-shadow: 0 10px 30px rgba(0,0,0,.35);
  }
  .card--front { top: 123px; }
  .card--back { top: 723px; }

  .brand {
    display: flex;
    align-items: center;
    gap: 18px;
  }
  .brand__dot {
    width: 54px; height: 54px;
    border-radius: 50%;
    border: 4px solid currentColor;
    flex: none;
  }
  .brand__name {
    font-weight: 300;
    text-transform: uppercase;
    letter-spacing: 0.18em;
    white-space: nowrap;
  }

  .card--front .brand {
    position: absolute;
    left: 0; right: 0; top: 128px;
    justify-content: center;
    color: var(--silver);
  }
  .card--front .brand__name { font-size: 34px; }

  .card--back .brand {
    position: absolute;
    left: 48px; top: 42px;
    color: var(--teal);
  }
  .card--back .brand__name { font-size: 32px; }

  .person {
    position: absolute;
    right: 360px; top: 142px;
    text-align: right;
  }
  .person__name {
    color: var(--teal);
    font-weight: 700;
    font-style: italic;
    font-size: 19px;
  }
  .person__role {
    color: var(--muted);
    font-size: 12px;
    margin-top: 4px;
  }
  .divider {
    position: absolute;
    left: 278px; top: 140px;
    width: 1px; height: 62px;
    background: var(--muted);
  }
  .contacts {
    position: absolute;
    left: 296px; top: 140px;
    list-style: none;
  }
  .contacts li {
    display: flex;
    align-items: center;
    gap: 12px;
    color: var(--stone);
    font-size: 14px;
    height: 21px;
  }
  .contacts svg { width: 13px; height: 13px; fill: var(--teal); flex: none; }
  .rule {
    position: absolute;
    left: 48px; right: 48px;
    height: 1px;
    background: var(--rule);
  }
  .rule--top { top: 124px; }
  .rule--bottom { top: 292px; }
  .tagline {
    position: absolute;
    left: 48px; top: 232px;
    color: var(--stone);
    font-size: 17px;
  }
</style>
</head>
<body>
  <section class="card card--front" aria-label="Card front">
    <div class="brand">
      <span class="brand__dot"></span>
      <span class="brand__name">Mabel’s Fitness</span>
    </div>
  </section>

  <section class="card card--back" aria-label="Card back">
    <div class="brand">
      <span class="brand__dot"></span>
      <span class="brand__name">Mabel’s Fitness</span>
    </div>
    <div class="rule rule--top"></div>
    <div class="person">
      <p class="person__name">Mabel Quint Harlow</p>
      <p class="person__role">Personal Trainer</p>
    </div>
    <div class="divider"></div>
    <ul class="contacts">
      <li>
        <svg viewBox="0 0 24 24" aria-hidden="true"><path d="M6.6 10.8a15.1 15.1 0 0 0 6.6 6.6l2.2-2.2c.3-.3.7-.4 1-.2 1.1.4 2.3.6 3.6.6.6 0 1 .4 1 1V20c0 .6-.4 1-1 1A17 17 0 0 1 3 4c0-.6.4-1 1-1h3.5c.6 0 1 .4 1 1 0 1.3.2 2.5.6 3.6.1.3 0 .7-.2 1z"/></svg>
        0781530462
      </li>
      <li>
        <svg viewBox="0 0 24 24" aria-hidden="true"><path d="M2 5h20v14H2zm2 2v.4l8 5 8-5V7zm0 2.8V17h16V9.8l-8 5z"/></svg>
        mabel@mabelsfitstudio.example
      </li>
      <li>
        <svg viewBox="0 0 24 24" aria-hidden="true"><path d="M12 2a10 10 0 1 0 0 20 10 10 0 0 0 0-20zm6.9 6h-3a15 15 0 0 0-1.3-3.9A8 8 0 0 1 18.9 8zM12 4c.8 1.2 1.5 2.5 1.9 4h-3.8c.4-1.5 1.1-2.8 1.9-4zM4.3 14a8 8 0 0 1 0-4h3.4a16 16 0 0 0 0 4zm.8 2h3a15 15 0 0 0 1.3 3.9A8 8 0 0 1 5.1 16zm3-8h-3a8 8 0 0 1 4.3-3.9C8.8 5.3 8.4 6.6 8.1 8zM12 20c-.8-1.2-1.5-2.5-1.9-4h3.8c-.4 1.5-1.1 2.8-1.9 4zm2.3-6H9.7a14 14 0 0 1 0-4h4.6a14 14 0 0 1 0 4zm.3 5.9c.6-1.2 1-2.5 1.3-3.9h3a8 8 0 0 1-4.3 3.9zM16.3 14a16 16 0 0 0 0-4h3.4a8 8 0 0 1 0 4z"/></svg>
        www.mabelsfitstudio.example
      </li>
    </ul>
    <p class="tagline">Become your happiest, healthiest and strongest self</p>
    <div class="rule rule--bottom"></div>
  </section>
</body>
</html>
```